Up to the Challenge? Canadian based consulting company needs a two sided business card design

A Canadian based security risk management consulting company needs a two-sided business card design. What we do is provide advice and guidance related to emergency, security and business continuity management for small, medium and large companies to help ensure the protection of their people, assets, information, services, operations and reputation.

The final design should be simple, only one or two colours, eye catching, professional and one that makes people look at three or more times just because it looks so darn good.

I have include examples of business cards I like.

Target Market(s)

Small, medium and large companies.

Industry/Entity Type

Security

Contact Information for Business Card

Business Card Size: Standard size of 3.5" (89mm) x 2.0" (51mm) - (see full specifications and guides on PRINTA's website if required)
Card Stock: Looking to use PRINTA's Velda 32pt stock textured paper - seam colour either chili red or black
Business Name: The Harrowfield Group
Website: www.theharrowfieldgroup.example
Telephone: (555)214-0397
Name: Dana Forsythe
Position: Principle
e-mail: Dana.Forsythe@theharrowfieldgroup.example

Font styles to use
Serif

Colors
ec1f27
000000
9d9d9d
aaaaaa
606060

Requirements
Must have
• - "The Harrowfield Group" logo (see uploaded files). I have included grey scale and colour versions.
• - Business card details (as above)
Nice to have
• - One side black or grey scale.
• - Other side would likely be white.
• - Everyone likes the silver logo on the black background.
• - Small element of colour i.e. red but I'm leaning more to greyscale.
Should not have
• - A lot of colour. Keep it simple.

```html
<!DOCTYPE html>
<html lang="en">
<head>
<meta charset="utf-8">
<title>The Harrowfield Group — Business Card</title>
<link href="https://fonts.googleapis.com/css2?family=Noto+Serif:wght@400;700&display=swap" rel="stylesheet">
<style>
  :root {
    --backdrop: #e9e7e4;
    --card-black: #2b2b2b;
    --card-white: #ffffff;
    --silver: #6f6f6f;
    --mark-grey: #aaaaaa;
    --ink: #3a3a3a;
    --ink-soft: #606060;
    --rule: #9d9d9d;
  }
  * { box-sizing: border-box; margin: 0; padding: 0; }
  html, body {
    width: 1200px; height: 1000px; overflow: hidden;
    background: var(--backdrop);
    font-family: "Noto Serif", Georgia, serif;
  }
  .canvas {
    width: 1200px; height: 1000px;
    display: flex; flex-direction: column;
    align-items: center; justify-content: center; gap: 60px;
  }
  .card {
    width: 665px; height: 380px;
    box-shadow: 0 6px 18px rgba(0,0,0,0.18);
    position: relative;
  }
  .card--front {
    background: var(--card-black);
    display: flex; flex-direction: column;
    align-items: center; justify-content: center; gap: 26px;
  }
  .brand-square {
    width: 86px; height: 86px;
    background: var(--silver);
  }
  .brand-name {
    color: var(--silver);
    font-size: 34px; font-weight: 400;
    letter-spacing: 2px; text-transform: uppercase;
  }
  .card--back {
    background: var(--card-white);
    display: flex; align-items: center;
    padding-left: 70px;
  }
  .back-square {
    width: 130px; height: 130px;
    background: var(--mark-grey);
    flex: none; margin-top: 60px;
  }
  .divider {
    width: 2px; height: 170px;
    background: var(--ink);
    margin: 0 26px 0 34px; flex: none;
  }
  .details { color: var(--ink); }
  .person-name {
    font-size: 24px; font-weight: 700;
    text-transform: uppercase; letter-spacing: 0.5px;
  }
  .person-role {
    font-size: 15px; text-transform: uppercase;
    color: var(--ink-soft); margin-bottom: 18px;
  }
  .contact-list { list-style: none; }
  .contact-item {
    display: flex; align-items: center; gap: 10px;
    font-size: 15px; line-height: 25px; color: var(--ink);
  }
  .contact-item svg { width: 13px; height: 13px; flex: none; fill: var(--ink); }
</style>
</head>
<body>
<main class="canvas">
  <section class="card card--front" aria-label="Card front">
    <div class="brand-square" aria-hidden="true"></div>
    <p class="brand-name">The Harrowfield Group</p>
  </section>

  <section class="card card--back" aria-label="Card back">
    <div class="back-square" aria-hidden="true"></div>
    <div class="divider" aria-hidden="true"></div>
    <div class="details">
      <h1 class="person-name">Dana Forsythe</h1>
      <p class="person-role">Principle</p>
      <ul class="contact-list">
        <li class="contact-item">
          <svg viewBox="0 0 16 16" aria-hidden="true"><path d="M3.6 1.2l2.3 2.6-1.3 2a9 9 0 0 0 5.6 5.6l2-1.3 2.6 2.3-1.5 2.2C7.4 14.8 1.2 8.6 1.4 2.7z"/></svg>
          (555)214-0397
        </li>
        <li class="contact-item">
          <svg viewBox="0 0 16 16" aria-hidden="true"><path d="M1 3h14v10H1z M2 4.2v.4l6 4 6-4v-.4z" fill-rule="evenodd"/></svg>
          dana.forsythe@theharrowfieldgroup.example
        </li>
        <li class="contact-item">
          <svg viewBox="0 0 16 16" aria-hidden="true"><circle cx="8" cy="8" r="7"/><path d="M1 8h14M8 1c-3 3-3 11 0 14M8 1c3 3 3 11 0 14" stroke="#fff" stroke-width="1" fill="none"/></svg>
          www.theharrowfieldgroup.example
        </li>
      </ul>
    </div>
  </section>
</main>
</body>
</html>
```